Brelvo Pizza & Pasta Takeaway Flyer

Our takeaway shop needs a well designed flyer for print and letter box distribution. Design to have a clear list of menu, Specials, contact details. If menu doesn't fit into A4, we won't mind going upto extended A4. I have attached draft copy of our menu and list of item in excel. Please add 5mm Bleed to the flyer.
Flyer will get printed on 115gsm Gloss stock.

```html
<!DOCTYPE html>
<html lang="en">
<head>
<meta charset="utf-8">
<title>Brelvo Pizza &amp; Pasta – Takeaway Menu</title>
<link href="https://fonts.googleapis.com/css2?family=Dancing+Script:wght@700&family=Open+Sans:ital,wght@0,400;0,600;1,600;1,700&display=swap" rel="stylesheet">
<style>
  :root{
    --green:#6cbd45;
    --red:#c0272d;
    --ink:#231f20;
    --paper:#ffffff;
    --veil:rgba(255,255,255,.80);
  }
  *{box-sizing:border-box;margin:0;padding:0}
  html,body{width:1200px;height:585px;overflow:hidden;background:var(--paper)}
  body{font-family:"Open Sans",Arial,sans-serif;color:var(--ink)}
  .menu{position:relative;width:1200px;height:585px}
  .panel{position:absolute;top:0;height:585px;overflow:hidden}
  .panel-photo{position:absolute;inset:0}
  .panel-photo::after{content:"";position:absolute;inset:0;background:var(--veil)}
  .starters .panel-photo{background:radial-gradient(circle at 70% 30%,#d9534a,#a8704e 45%,#6b5140)}
  .pizzas .panel-photo{background:radial-gradient(circle at 40% 60%,#e2b86a,#c98a4c 45%,#9e6a48)}
  .premium .panel-photo{background:radial-gradient(circle at 50% 40%,#d8a25c,#b1824f 50%,#8a7060)}
  .pastas .panel-photo{background:linear-gradient(160deg,#d8cfc4,#c9b48c 50%,#b8a89a)}
  .panel-body{position:relative;height:100%}

  .tab{position:absolute;height:30px;background:var(--green);color:#fff;
       font-family:"Dancing Script",cursive;font-size:27px;line-height:30px;text-align:center;white-space:nowrap}
  .tab-right{clip-path:polygon(0 0,100% 0,93% 100%,0 100%)}
  .tab-left{clip-path:polygon(7% 0,100% 0,100% 100%,0 100%)}
  .tab small{font-family:"Open Sans",sans-serif;font-style:italic;font-weight:700;font-size:10px;vertical-align:middle;margin-left:6px}

  .list{position:absolute;left:22px;right:10px}
  .item{display:grid;grid-template-columns:1fr auto;column-gap:6px}
  .name{color:var(--red);font-size:12.5px;line-height:16px;white-space:nowrap}
  .name em{font-style:italic;font-weight:700}
  .price{color:var(--red);font-size:13px;font-weight:600;line-height:16px;text-align:right}
  .desc{grid-column:1 / -1;font-size:7.2px;line-height:9.5px;margin-bottom:3px}
  .note{color:var(--red);font-style:italic;font-weight:700;font-size:10.5px;line-height:14px}

  .list.roomy .name,.list.roomy .price{line-height:17.5px}
  .list.tight .name,.list.tight .price{line-height:15px}
  .list.tight .desc{line-height:8.5px;margin-bottom:2px}

  .sizes{position:absolute;display:grid;grid-template-columns:88px 64px 64px 64px;align-items:center;color:var(--red);font-weight:600;text-align:center}
  .sizes .range{text-align:left;font-size:13px;letter-spacing:.5px}
  .sizes .size{font-size:13.5px;line-height:16px}
  .sizes .size b{display:block;font-size:14.5px;font-weight:600}

  .sub-price{position:absolute;left:236px;top:400px;color:var(--red);font-weight:600;font-size:13px}
  .calzone-text{position:absolute;left:14px;right:12px;top:487px;text-align:center}
</style>
</head>
<body>
<main class="menu">

  <section class="panel starters" style="left:0;width:300px">
    <div class="panel-photo" role="img" aria-label="Faded photo of tomatoes, herbs and a glass of drink"></div>
    <div class="panel-body">
      <h2 class="tab tab-right" style="left:0;top:12px;width:238px">Starter</h2>
      <div class="list roomy" style="top:41px">
        <div class="item"><span class="name">Garlic Bread</span><span class="price">$3.95</span></div>
        <div class="item"><span class="name">Cheesy Garlic Bread</span><span class="price">$5.50</span></div>
        <div class="item"><span class="name">Sweet Chilli Cheese Pizza</span><span class="price">$7.95</span><span class="desc">Sweet Chilli Sauce Base topped with Cheese &amp; Herbs</span></div>
        <div class="item"><span class="name">Chips <em>(Lge +$2)</em></span><span class="price">$4.95</span><span class="desc">With Tomato Sauce</span></div>
        <div class="item"><span class="name">Chips &amp; Gravy</span><span class="price">$6.95</span></div>
        <div class="item"><span class="name">Beer Battered Chips</span><span class="price">$6.95</span></div>
        <div class="item"><span class="name">Curly Fries <em>(Lge +$2.5)</em></span><span class="price">$5.95</span><span class="desc">With Ranch Dip</span></div>
        <div class="item"><span class="name">Sweet Potato Chips</span><span class="price">$6.95</span><span class="desc">With Garlic Aioli Sauce</span></div>
        <div class="item"><span class="name">Onion Rings</span><span class="price">$6.50</span><span class="desc">With Ranch Dip</span></div>
        <div class="item"><span class="name">Chicken Nugget <em>(8 Pcs)</em></span><span class="price">$4.95</span><span class="desc">With Tomato Sauce</span></div>
        <div class="item"><span class="name">Pepper Squid</span><span class="price">$.......</span></div>
        <div class="item"><span class="name">Beef Chilli</span><span class="price">$7.95</span><span class="desc">With Lemon Wedge</span></div>
        <div class="item"><span class="name">Chicken Lollipop</span><span class="price">$7.95</span><span class="desc">With Garlic Aioli Sauce</span></div>
        <p class="note" style="padding-left:22px">** Add Extra Sauce $0.75</p>
      </div>

      <h2 class="tab tab-right" style="left:0;top:396px;width:215px">Garlic Sub</h2>
      <span class="sub-price">$9.95</span>
      <div class="list" style="top:434px">
        <div class="item"><span class="name">Pulled Beef</span><span></span><span class="desc">Cheese, Pulled Beef, Salami, Onion, Mushroom with BBQ Sauce</span></div>
        <div class="item"><span class="name">Chicken</span><span></span><span class="desc">Cheese, Seasoned Chicken, Tomato, Onion, Fetta with Sweet Chilli Sauce</span></div>
        <div class="item"><span class="name">Veg</span><span></span><span class="desc">Cheese, Tomato, Onion, Mushroom, Capsicum, Pineapple with Tomato Sauce</span></div>
        <div class="item"><span class="name">Meat</span><span></span><span class="desc">Cheese, Ham, Pepperoni, Salami, Sausage with BBQ Sauce</span></div>
        <div class="item"><span class="name">Bacon &amp; Chicken</span><span></span><span class="desc">Cheese, Seasoned Chicken, Bacon, Mushroom with Peri Peri Sauce</span></div>
      </div>
    </div>
  </section>

  <section class="panel pizzas" style="left:306px;width:296px">
    <div class="panel-photo" role="img" aria-label="Faded photo of a baked pizza"></div>
    <div class="panel-body">
      <h2 class="tab tab-right" style="left:0;top:12px;width:224px">Pizza</h2>
      <div class="sizes" style="left:16px;top:42px">
        <span class="range">LITE</span>
        <span class="size">Small<b>$9</b></span><span class="size">Large<b>$15</b></span><span class="size">Family<b>$20</b></span>
      </div>
      <div class="list" style="top:74px;left:11px">
        <div class="item"><span class="name">Hawaiian</span><span></span><span class="desc">Cheese, Ham &amp; Pineapple</span></div>
        <div class="item"><span class="name">Margherita</span><span></span><span class="desc">Cheese, Tomatoes, Basil &amp; Oregano</span></div>
        <div class="item"><span class="name">Mozzy</span><span></span><span class="desc">Cheese, Basil &amp; Oregano</span></div>
        <div class="item"><span class="name">New Yorker</span><span></span><span class="desc">Pepperoni, Basil &amp; Oregano</span></div>
        <div class="item"><span class="name">Veggie</span><span></span><span class="desc">Onion, Tomato, Mushroom, Capsicum, Olives, Pineapple, Basil and Oregano</span></div>
      </div>
      <div class="sizes" style="left:16px;top:232px">
        <span class="range">CLASSIC</span>
        <span class="size">Small<b>$11</b></span><span class="size">Large<b>$17</b></span><span class="size">Family<b>$22</b></span>
      </div>
      <div class="list tight" style="top:268px;left:11px">
        <div class="item"><span class="name">Supreme</span><span></span><span class="desc">Cheese, Pepperoni, Ham, Beef , Onion, Olives, Capsicum, Pineapple &amp; Mushroom</span></div>
        <div class="item"><span class="name">Meat Lovers</span><span></span><span class="desc">Cheese, Pepperoni, Salami, Ham, Bacon, Sausage &amp; BBQ Sauce</span></div>
        <div class="item"><span class="name">Ozzy</span><span></span><span class="desc">Cheese, Sausage, Bacon, Onion &amp; Egg</span></div>
        <div class="item"><span class="name">BBQ Chicken</span><span></span><span class="desc">Cheese, Chicken, Bacon, Mushroom &amp; BBQ Sauce</span></div>
        <div class="item"><span class="name">Tropical Chicken</span><span></span><span class="desc">Cheese, Chicken, Ham, Pineapple</span></div>
        <div class="item"><span class="name">Outback</span><span></span><span class="desc">Cheese, Ham, Salami, Bacon , Mushroom &amp; Onion</span></div>
        <div class="item"><span class="name">Spicy Pizza</span><span></span><span class="desc">Cheese, Pepperoni, Onion, Jalapenos &amp;Chilli Flakes</span></div>
        <div class="item"><span class="name">Mexican</span><span></span><span class="desc">Cheese, Beef, Pepperoni, Onion, Roasted Capsicum, Jalapenos, Chilli &amp; Sour cream</span></div>
        <div class="item"><span class="name">Capricciosa</span><span></span><span class="desc">Cheese, Ham, Salami, Mushroom, Tomato &amp; Olives</span></div>
        <div class="item"><span class="name">Veg Supreme</span><span></span><span class="desc">Cheese, Tomato, Onion, Mushroom, Roasted Capsicum, Pineapple, Fetta, Jalapenos &amp; Chilli</span></div>
        <div class="item"><span class="name">Four Cheese</span><span></span><span class="desc">Cheese, Fetta, Bocconcini, Parmesan &amp; Basil</span></div>
      </div>
    </div>
  </section>

  <section class="panel premium" style="left:608px;width:296px">
    <div class="panel-photo" role="img" aria-label="Faded photo of a pizza topped with olives and capsicum"></div>
    <div class="panel-body">
      <div class="sizes" style="left:14px;top:17px">
        <span class="range">PREMIUM</span>
        <span class="size">Small<b>$13</b></span><span class="size">Large<b>$19</b></span><span class="size">Family<b>$25</b></span>
      </div>
      <div class="list tight" style="top:52px;left:6px">
        <div class="item"><span class="name">Garden Gourmet</span><span></span><span class="desc">Cheese, Semi-dried tomato, Mushrooms, Onion, Roasted Capsicum, Olives, Cherry Tomato, Spinach, Bocconcini &amp; Basil</span></div>
        <div class="item"><span class="name">Paneer Tikka</span><span></span><span class="desc">Cheese, Marinated Paneer, Onion, Tomato, Capsicum, Olives &amp; Corinander</span></div>
        <div class="item"><span class="name">Pesto Chicken</span><span></span><span class="desc">Cheese, Chicken, Sun-Dried Tomato, Onion, Fetta &amp; Parsley</span></div>
        <div class="item"><span class="name">Butter Chicken</span><span></span><span class="desc">Cheese, Marinated Chicken, Onion, Capsicum, Corinder, Cashew &amp; Lemon Wedge</span></div>
        <div class="item"><span class="name">Meat &amp; Chicken</span><span></span><span class="desc">Pulled Beef, Pepperoni, Chicken, Salami, Roasted Capsicum, Mushroom, Onion &amp; BBQ Sauce</span></div>
        <div class="item"><span class="name">Mediterranean</span><span></span><span class="desc">Cheese, Roasted Capsicum, Mushroom, Sausage, Olives, Fetta &amp; Bocconcini</span></div>
        <div class="item"><span class="name">The Lot</span><span></span><span class="desc">Ham, Pepperoni, Salami, Pulled Beef, Sausage, Capsicum, Onion, Olives, Tomato, Pineapple, Basil &amp; Oregano</span></div>
      </div>
      <div class="sizes" style="left:14px;top:274px">
        <span class="range">PREMIUM</span>
        <span class="size">Small<b>$14</b></span><span class="size">Large<b>$21</b></span><span class="size">Family<b>$28</b></span>
      </div>
      <div class="list" style="top:308px;left:6px">
        <div class="item"><span class="name">The Pacific</span><span></span><span class="desc">Seafood Mix , Mushrooms, Roasted Capsicum &amp; Garlic Oil (Anchovies Suggested)</span></div>
        <div class="item"><span class="name">Reef n Turf</span><span></span><span class="desc">Prawn, Pulled Beef, Onion, Mushroom, Capsicum, Olives &amp; Garlic Sauce</span></div>
        <div class="item"><span class="name">Prawn &amp; Garlic</span><span></span><span class="desc">Prawns, Cheery Tomato, Spinach, Bocconcini &amp; Garlic Sauce</span></div>
        <p class="note" style="margin-top:6px;font-size:9.5px">** Thin Base Available **<br>** GF base available only in large size. Extra $3 **<br>** Each Extra Topping - Small $1, Large $2, Family $3 **</p>
      </div>

      <h2 class="tab tab-right" style="left:0;top:452px;width:222px">Calzone</h2>
      <p class="note calzone-text" style="font-size:10px;line-height:13px">*Folded Pizza, Rolled &amp; Cooked, Sealing in All Flaours.<br>Simply Select from Classic and Premium Pizza range.*</p>
      <div class="list" style="top:530px;left:6px">
        <div class="item"><span class="name">Classic Calzone</span><span class="price">$16</span></div>
        <div class="item"><span class="name">Premium Calzone</span><span class="price">$18</span></div>
      </div>
    </div>
  </section>

  <section class="panel pastas" style="left:904px;width:296px">
    <div class="panel-photo" role="img" aria-label="Faded photo of pasta on a wooden table"></div>
    <div class="panel-body">
      <h2 class="tab tab-left" style="right:10px;top:12px;width:214px">Pasta</h2>
      <div class="list tight" style="top:42px;left:8px;right:16px">
        <div class="item"><span class="name">Napoletana</span><span class="price">$14</span><span class="desc">Tomatoes, Onions, and Special Italian Herbs in Red Pasta sauce.</span></div>
        <div class="item"><span class="name">Vegetaria</span><span class="price">$16</span><span class="desc">Mushroom, Tomatoes, Onions,Capsicum and Special Italian Herbs in Red Pasta sauce.</span></div>
        <div class="item"><span class="name">Bolognese</span><span class="price">$16</span><span class="desc">Traditional Beef, Onions and Special Italian Herbs in Red Pasta sauce.</span></div>
        <div class="item"><span class="name">Carbonara</span><span class="price">$16</span><span class="desc">Bacon, Eggs &amp; Mushrooms in a Creamy White Sauce.</span></div>
        <div class="item"><span class="name">Alla Panna</span><span class="price">$16</span><span class="desc">Ham &amp; Mushrooms in a Creamy White Sauce.</span></div>
        <div class="item"><span class="name">Chicken Carbonara</span><span class="price">$16</span><span class="desc">Chicken, Eggs, Mushrooms &amp; Onions in a Creamy White Sauce.</span></div>
        <div class="item"><span class="name">Chicken Pesto</span><span class="price">$16</span><span class="desc">Chicken, Tomato, Pesto in a Creamy White Sauce.</span></div>
        <div class="item"><span class="name">Greek Chicken</span><span class="price">$16</span><span class="desc">Chicken, Tomato, Fetta, Olives in a Red Pasta Sauce.</span></div>
        <div class="item"><span class="name">Garlic Prawn</span><span class="price">$18</span><span class="desc">Prawn, Garlic, Onion, Lemon in a Creamy White Sauce.</span></div>
        <div class="item"><span class="name">Puttanesca</span><span class="price">$18</span><span class="desc">Anchovies, Olives, Capers in a Red Pasta Sauce.</span></div>
        <div class="item"><span class="name">Marinara</span><span class="price">$18</span><span class="desc">Seafood mix in a Red Pasta Sauce.</span></div>
      </div>

      <h2 class="tab tab-right" style="left:0;top:349px;width:268px;text-align:left;padding-left:12px">Main<small>(Served with Chips &amp; Garden Salad)</small></h2>
      <div class="list tight" style="top:381px;left:8px;right:16px">
        <div class="item"><span class="name">Chicken Schnitzel with Gravy</span><span class="price">$16</span></div>
        <div class="item"><span class="name">Veal Schnitzel with Gravy</span><span class="price">$16</span></div>
        <div class="item"><span class="name">Chicken Parmigianna</span><span class="price">$17</span></div>
        <div class="item"><span class="name">Three Cheese Parmigianna</span><span class="price">$17</span><span class="desc">Topped with Parmesan, Mozzarella, Bocconcini &amp; Herbs</span></div>
        <div class="item"><span class="name">Hawiian Parmigianna</span><span class="price">$17</span><span class="desc">Topped with Cheese, Ham, Pineapple &amp; Herbs</span></div>
        <div class="item"><span class="name">Mexican Parmigianna</span><span class="price">$17</span><span class="desc">Topped with Cheese, Roasted Capsicum, Jalapenos &amp; Herbs</span></div>
        <div class="item"><span class="name">Marinara Parmigianna</span><span class="price">$19</span><span class="desc">Topped with Cheese, Seafood mix &amp; Herbs</span></div>
        <div class="item"><span class="name">Creamy Garlic Prawn</span><span class="price">$19</span><span class="desc">Tiger Prawn, Garlic, White Wine, Spices &amp; Herbs Pan fried with Creamy sauce</span></div>
      </div>
    </div>
  </section>

</main>
</body>
</html>
```